Crowdsourced Research Platform: KOVAL Polls

KOVAL Polls is an acronym for Kindred Opinion Views Among Lands (KOVAL) Polls. This is a research effort to format and combine multiple sources of public opinion data from around the world into merged datasets. The website will at first mainly act as a quality control hub and distribution point for official dataset releases. It will provide resources such as codebooks, development guidelines, and instructional videos for crowdsourcing continued expansion of the resource. We need a coded (HTML and CSS) website design and associated files to launch the website with ease. We purchased the domain www.kovalpolls.org, but access is blocked while it is under construction.

The website design should be based on a logo recently commissioned (see attached). The design should be simple and professional with lots of white space. We would like the logo on the top left of all pages and the primary navigation menu along the top-right of all pages. The primary navigation menu should have a simple mouse-over effect and the main menu items should expand with secondary drop-down options. The footer should include a few columns with headings and links to different pages. The website layout should be dynamic and expand its width to fit different sized screens. There will be a lot of data and information displayed in tables, so we would like the CSS coding and website design to include tables designed to match the website theme. The main graphical content will be data visualisations such as pie/bar charts, histograms, scatter plots, heat maps, moving average trend lines etc. We would therefore like the design to include modular sections (boxes matching theme to display plots/graphs/etc) that can visually display these types of figures with text/caption underneath to explain the data visualizations.

For more information and written placeholder content, designers should read the attached documents to get a better idea about the project. Some draft working papers using merged datsets have been included for reference and you can use these for their examples of data visualizations and use the written content for filling in page content.

Target Market(s)

The primary target audience will be academics in universities and research institutes. The resource will be most useful to quantitative social scientists, particularly political scientists and sociologists, but any discipline concerned with us humans could find the resource useful. Others such as graduate-level university students, civil servants in government departments, members of research institutions, and policy researchers in non-profit organizations will also find the resource useful.

Coding

Coded - Design and coding required

Number of Pages Required

3 page

Font styles to use
Sans Serif

Colors

Designer to choose colors to be used in the design.

Requirements
Must have
• HTML and CSS coding (not Wordpress)
Nice to have
• Content boxes to display data visualizations alongside articles.

```html
<!DOCTYPE html>
<html lang="en">
<head>
<meta charset="utf-8">
<title>KOVAL Polls — Re-imagining Surveys</title>
<link rel="stylesheet" href="https://fonts.googleapis.com/css2?family=Arimo:wght@400;500&display=swap">
<style>
  :root {
    --backdrop-left: #a767d6;
    --backdrop-left-deep: #7a5fb8;
    --backdrop-right: #8cbfdc;
    --backdrop-right-deep: #79d6cc;
    --page-white: #ffffff;
    --page-foot: #f8f8fc;
    --hero-violet: #9a22ee;
    --hero-blue: #6a9ed8;
    --photo-sky: #b4b0a6;
    --photo-sea: #9aa3a3;
    --photo-meadow: #5d7a35;
    --photo-grass: #6f8c3c;
    --ink-heading: #2a2a2a;
    --ink-body: #6d6d6d;
    --ink-button: #2b2f6e;
    --accent-teal: #6fd6c7;
    --button-line: #e6e6ee;
    --ink-light: #ffffff;
  }

  * { box-sizing: border-box; margin: 0; padding: 0; }

  html, body {
    width: 1200px;
    height: 591px;
    overflow: hidden;
  }

  body {
    position: relative;
    font-family: "Arimo", Arial, sans-serif;
    background: var(--page-white);
  }

  .backdrop {
    position: absolute;
    top: 0;
    height: 591px;
  }
  .backdrop--left {
    left: 0;
    width: 150px;
    background: linear-gradient(180deg, var(--backdrop-left) 0%, var(--backdrop-left-deep) 100%);
  }
  .backdrop--right {
    right: 0;
    width: 152px;
    background: linear-gradient(180deg, var(--backdrop-right) 0%, var(--backdrop-right-deep) 100%);
  }

  .page {
    position: absolute;
    left: 150px;
    top: 0;
    width: 898px;
    height: 591px;
    background: var(--page-white);
  }

  .page__foot {
    position: absolute;
    left: 0;
    top: 506px;
    width: 100%;
    height: 85px;
    background: var(--page-foot);
  }

  .hero {
    position: absolute;
    left: 0;
    top: 79px;
    width: 898px;
    height: 427px;
  }

  .hero__brand-panel {
    position: absolute;
    left: 0;
    top: 0;
    width: 450px;
    height: 427px;
    background: linear-gradient(135deg, var(--hero-violet) 0%, var(--hero-blue) 100%);
  }

  .hero__photo {
    position: absolute;
    left: 450px;
    top: 0;
    width: 448px;
    height: 427px;
    background: linear-gradient(180deg,
      var(--photo-sky) 0%,
      var(--photo-sea) 22%,
      var(--photo-meadow) 45%,
      var(--photo-grass) 100%);
  }

  .hero__title {
    position: absolute;
    left: 13px;
    top: 193px;
    color: var(--ink-light);
    font-size: 21px;
    font-weight: 400;
    line-height: 24px;
  }

  .hero__tagline {
    position: absolute;
    left: 13px;
    top: 222px;
    color: var(--ink-light);
    font-size: 12.5px;
    letter-spacing: 0.1px;
    text-transform: uppercase;
  }

  .intro-card {
    position: absolute;
    left: 238px;
    top: 81px;
    width: 422px;
    height: 266px;
    background: var(--page-white);
    border-radius: 2px;
    padding: 56px 80px 0 80px;
  }

  .intro-card__heading {
    font-size: 12.5px;
    font-weight: 400;
    color: var(--ink-heading);
    text-transform: uppercase;
    letter-spacing: 0.1px;
    line-height: 16px;
  }

  .intro-card__text {
    margin-top: 13px;
    font-size: 12.5px;
    line-height: 18.7px;
    color: var(--ink-body);
  }

  .intro-card__button {
    display: inline-flex;
    align-items: center;
    gap: 10px;
    margin-top: 16px;
    height: 36px;
    width: 142px;
    padding-left: 27px;
    border: 1px solid var(--button-line);
    border-radius: 18px;
    background: var(--page-white);
    color: var(--ink-button);
    font-family: inherit;
    font-size: 12.5px;
    text-decoration: none;
  }

  .intro-card__arrow {
    width: 14px;
    height: 10px;
  }
</style>
</head>
<body>
  <div class="backdrop backdrop--left" role="img" aria-label="Soft-focus photo of a person using a phone, tinted violet"></div>
  <div class="backdrop backdrop--right" role="img" aria-label="Soft-focus photo of a person outdoors, tinted teal"></div>

  <main class="page">
    <section class="hero">
      <div class="hero__brand-panel">
        <h1 class="hero__title">KOVAL Polls</h1>
        <p class="hero__tagline">Re-imagining surveys</p>
      </div>

      <div class="hero__photo" role="img" aria-label="Photo of a person in a knit hat sitting on a grassy hill above a coastline"></div>

      <article class="intro-card">
        <h2 class="intro-card__heading">From the part of beginning</h2>
        <p class="intro-card__text">The ultimate goal is to format every variable from every round of every publicly available survey source that takes nationally representative samples of adults. .</p>
        <a class="intro-card__button" href="#">
          Get Started
          <svg class="intro-card__arrow" viewBox="0 0 14 10" aria-hidden="true">
            <path d="M0 5 H12.5 M8.5 1 L12.5 5 L8.5 9" fill="none" stroke="var(--accent-teal)" stroke-width="1.2"/>
          </svg>
        </a>
      </article>
    </section>

    <div class="page__foot"></div>
  </main>
</body>
</html>
```